Coffee label for coffee brand - Kiln Lantern coffee

We want someone to design a label for packaging of a coffee line. The design will then be printed on stickers.

It is called Kiln Lantern Coffee (logo enclosed) I want to incorporate a streetscape and the idea is that with every different coffee it will be a different colour (we have 6 varieties at the moment) with a black background. It needs to have a modern feel.

It needs to have a blank area towards the bottom for the type of coffee which we will print later on)

text to include

'Roasting exceptional coffee'

Target Market(s)

Coffee drinkers - modern feel

Font styles to use
Sans Serif

Colors
f78f20
9bcb3b
33a6d7
b768aa

Requirements
Must have
• the logo incorporated
• Space for coffee variety
• Quote' Roasting exceptional coffee'
Nice to have
• Streetscape theme incorporated - bright colour varieties (would love metallic) (on black background)

```html
<!DOCTYPE html>
<html lang="en">
<head>
<meta charset="utf-8">
<title>Kiln Lantern Coffee – Label</title>
<link rel="stylesheet" href="https://fonts.googleapis.com/css2?family=PT+Sans:wght@400;700&family=Kalam:wght@400&display=swap">
<style>
  :root {
    --page-bg: #5f5c5a;
    --label-top: #2b1d15;
    --label-mid: #3e2a1d;
    --label-bottom: #6d4c31;
    --title-tan: #c58c57;
    --band-dark: #3f2216;
    --band-light: #6e3d25;
    --pill-fill: #b27a4e;
    --cream: #f4ede4;
    --skyline-tone-a: #4a3323;
    --skyline-tone-b: #7a5638;
  }
  * { box-sizing: border-box; margin: 0; padding: 0; }
  html, body { width: 1200px; height: 857px; overflow: hidden; }
  body {
    background: var(--page-bg);
    display: flex;
    align-items: center;
    justify-content: center;
  }
  .label {
    position: relative;
    width: 495px;
    height: 800px;
    border-radius: 36px;
    overflow: hidden;
    background: linear-gradient(180deg, var(--label-top) 0%, var(--label-mid) 40%, var(--label-bottom) 100%);
  }
  .skyline-art {
    position: absolute;
    left: 110px;
    top: 42px;
    width: 260px;
    height: 110px;
    background: linear-gradient(180deg, rgba(255,255,255,0.10), rgba(255,255,255,0.02));
    border-radius: 6px;
  }
  .brand-name {
    position: absolute;
    left: 0; right: 0;
    top: 168px;
    display: flex;
    align-items: center;
    justify-content: center;
    gap: 14px;
    font-family: "PT Sans", sans-serif;
    font-weight: 700;
    font-size: 56px;
    color: var(--cream);
    letter-spacing: 1px;
  }
  .brand-dot {
    width: 22px; height: 22px;
    border-radius: 50%;
    background: var(--cream);
  }
  .brand-title {
    position: absolute;
    left: 0; right: 0;
    top: 336px;
    text-align: center;
    font-family: "Kalam", cursive;
    font-size: 42px;
    color: var(--title-tan);
    letter-spacing: 1px;
  }
  .tagline-band {
    position: absolute;
    left: 0; right: 0;
    top: 419px;
    height: 54px;
    display: flex;
    align-items: center;
    justify-content: center;
    background: linear-gradient(90deg, var(--band-dark), var(--band-light) 50%, var(--band-dark));
    font-family: "PT Sans", sans-serif;
    font-size: 27px;
    color: var(--cream);
  }
  .variety-pill {
    position: absolute;
    left: 142px;
    top: 519px;
    width: 211px;
    height: 38px;
    border-radius: 10px;
    display: flex;
    align-items: center;
    justify-content: center;
    background: var(--pill-fill);
    font-family: "PT Sans", sans-serif;
    font-size: 21px;
    color: var(--cream);
  }
  .street-scene {
    position: absolute;
    left: 0; right: 0;
    bottom: 0;
    height: 227px;
    background: linear-gradient(180deg, rgba(74,51,35,0) 0%, var(--skyline-tone-a) 45%, var(--skyline-tone-b) 100%);
    opacity: 0.55;
  }
</style>
</head>
<body>
  <main class="label">
    <div class="skyline-art" role="img" aria-label="Line drawing of a city skyline above the brand name"></div>
    <div class="brand-name"><span class="brand-dot"></span>Kiln Lantern</div>
    <h1 class="brand-title">Kiln Lantern Coffee</h1>
    <div class="tagline-band">Roasting Exceptional Coffee</div>
    <div class="variety-pill">For Coffee Variety</div>
    <div class="street-scene" role="img" aria-label="Faint streetscape with scattered coffee beans"></div>
  </main>
</body>
</html>
```